HANDYMAN SERVICES

we provide a good,and reliable service.we do all aspects of home improvement ,also all garden services,and any repairs,no job too small,free quotes .
I am aiming towards the general public for clients,also be doing special rates for the elderly,and reducing the price for anyone who does a friend reference. It will be free quotes/consultation,all work will be guaranteed.
Now the type of work we do is cctv installation,decking,patio/driveway cleaning,garages for erecting/repairs,house/garage clearances,fit alarm systems,fit or repair windows/doors,lay patios,repair roofs,decorate interior/external,erect ariaels,lay driveways,erect or repair fencing,lay drainage,repair or erect guttering and soffits,water features,erect or repair kitchens/bathrooms,also plastering,lay lawns or repair,also repair/erect sheds.
Home Improvement

```html
<!DOCTYPE html>
<html lang="en">
<head>
<meta charset="utf-8">
<title>Handyman Services Flyer</title>
<link rel="stylesheet" href="https://fonts.googleapis.com/css2?family=Archivo+Black&family=Gelasio:wght@700&family=Kanit:wght@500;600&family=Oswald:wght@600;700&family=Roboto:wght@700;900&display=swap">
<style>
  :root {
    --red: #e1232a;
    --red-dark: #b8161c;
    --band: #34383b;
    --white: #ffffff;
    --ink: #2d2f31;
    --title-grey: #4a4d50;
    --sky-top: #a9d6ee;
    --sky-bottom: #ffffff;
    --sand: #f6dcaa;
    --tick: #e4561c;
    --gold: #f4b41a;
    --gold-light: #fbd35b;
    --blue: #1f82c9;
    --blue-dark: #0f5f9e;
  }
  * { box-sizing: border-box; margin: 0; padding: 0; }
  html, body { width: 1200px; height: 884px; overflow: hidden; background: #ffffff; }

  .flyer {
    position: relative;
    width: 1200px;
    height: 884px;
    overflow: hidden;
    background: linear-gradient(180deg, var(--sky-top) 0%, #d7ecf7 55%, var(--sky-bottom) 85%);
  }

  /* Header */
  .header {
    position: absolute; left: 0; top: 0; width: 100%; height: 228px;
    background: linear-gradient(180deg, #ee2d32 0%, var(--red) 70%, var(--red-dark) 100%);
  }
  .header__ruler {
    position: absolute; left: 0; bottom: 0; width: 100%; height: 26px;
    background: repeating-linear-gradient(90deg, rgba(120,10,14,.55) 0 2px, transparent 2px 34px);
    -webkit-mask: linear-gradient(180deg, transparent 0, #000 100%);
            mask: linear-gradient(180deg, transparent 0, #000 100%);
  }
  .title {
    position: absolute; left: 50px; top: 70px;
    font-family: "Archivo Black", sans-serif;
    font-size: 102px; line-height: 1; letter-spacing: -1px;
    color: var(--white); white-space: nowrap;
    text-shadow: 0 4px 0 #9a9da0, 0 7px 8px rgba(0,0,0,.45);
  }
  .title__sub {
    position: absolute; left: 660px; top: 74px;
    font-family: "Archivo Black", sans-serif;
    font-size: 50px; line-height: 1; letter-spacing: 1px;
    color: var(--title-grey); white-space: nowrap;
    -webkit-text-stroke: 3px var(--white);
    paint-order: stroke fill;
    text-shadow: 0 4px 6px rgba(0,0,0,.35);
  }

  /* Service band */
  .band {
    position: absolute; left: 0; top: 228px; width: 100%; height: 64px;
    background: var(--band);
    border-bottom: 4px solid #222;
    display: flex; align-items: center; padding-left: 48px; gap: 14px;
    font-family: "Gelasio", serif; font-weight: 700;
    font-size: 32px; color: var(--white); letter-spacing: .5px;
  }
  .band__dot { width: 11px; height: 11px; border-radius: 50%; background: var(--red); }

  /* Senior badge */
  .badge { position: absolute; left: 950px; top: 88px; width: 210px; height: 210px; z-index: 3; }
  .badge__ray {
    position: absolute; left: 30px; top: 30px; width: 150px; height: 150px;
    background: var(--gold);
  }
  .badge__ray:nth-child(2) { transform: rotate(22.5deg); }
  .badge__ray:nth-child(3) { transform: rotate(45deg); }
  .badge__ray:nth-child(4) { transform: rotate(67.5deg); }
  .badge__disc {
    position: absolute; left: 22px; top: 22px; width: 166px; height: 166px; border-radius: 50%;
    background: radial-gradient(circle at 40% 35%, var(--gold-light), var(--gold) 75%);
    border: 3px solid #e59b0c;
  }
  .badge__art {
    position: absolute; left: 62px; top: 38px; width: 86px; height: 90px; border-radius: 10px;
    background: #d9541f; opacity: .85;
  }
  .badge__ribbon {
    position: absolute; left: 20px; top: 138px; width: 170px; height: 46px;
    background: #fbe7a1; border: 2px solid #e0a11a; border-radius: 6px;
    font-family: "Roboto", sans-serif; font-weight: 700; font-size: 12.5px; line-height: 1.2;
    color: var(--red-dark); text-align: center; padding-top: 6px;
  }

  /* Left column */
  .side {
    position: absolute; left: 0; top: 296px; width: 290px; height: 588px;
    background: linear-gradient(180deg, var(--sand) 0%, #fbeedd 60%, rgba(255,255,255,0) 100%);
  }
  .refer {
    position: absolute; left: 66px; top: 318px; width: 206px; height: 206px; border-radius: 50%;
    background: radial-gradient(circle at 50% 40%, #3aa4e6, var(--blue) 60%, var(--blue-dark));
    border: 6px solid var(--white);
    box-shadow: 0 4px 10px rgba(0,0,0,.3);
    text-align: center; color: var(--white);
    font-family: "Roboto", sans-serif; font-weight: 900;
  }
  .refer__icon {
    width: 96px; height: 34px; margin: 22px auto 6px; border-radius: 16px 16px 4px 4px;
    background: #cde8f8;
  }
  .refer__line { display: block; font-size: 40px; line-height: .95; letter-spacing: -1px; }
  .refer__small { display: block; font-size: 15px; margin-top: 6px; letter-spacing: .5px; }
  .worker {
    position: absolute; left: 98px; top: 560px; width: 240px; height: 300px;
    border-radius: 40% 40% 20% 20%;
    background: linear-gradient(180deg, #f3c49a 0%, #3d6fc2 45%, #2b55a2 100%);
    opacity: .9;
  }

  /* Service lists */
  .services { position: absolute; font-family: "Kanit", sans-serif; }
  .services__heading {
    font-family: "Oswald", sans-serif; font-weight: 700;
    font-size: 34px; color: var(--red); letter-spacing: .5px; margin-bottom: 4px;
  }
  .services__list { list-style: none; }
  .services__item {
    position: relative; padding-left: 30px;
    font-weight: 500; font-size: 22px; line-height: 33px; color: var(--ink);
  }
  .services__item::before {
    content: ""; position: absolute; left: 6px; top: 9px;
    width: 9px; height: 16px;
    border-right: 4px solid var(--tick); border-bottom: 4px solid var(--tick);
    transform: rotate(40deg);
  }
  .services--left { left: 330px; top: 325px; }
  .services--right { left: 718px; top: 322px; }

  /* Footer */
  .slogan {
    position: absolute; left: 330px; top: 720px; width: 270px; height: 130px;
    border-radius: 18px; background: #f8e32a;
    transform: rotate(-6deg);
  }
  .call { position: absolute; left: 600px; top: 728px; }
  .call__icon { position: absolute; left: 0; top: 0; width: 88px; height: 88px; }
  .call__pill {
    position: absolute; left: 70px; top: 6px; width: 238px; height: 40px;
    background: var(--band); border-radius: 0 20px 20px 0;
    color: var(--white); font-family: "Roboto", sans-serif; font-weight: 700;
    font-size: 22px; line-height: 40px; text-align: center;
  }
  .call__number {
    position: absolute; left: 82px; top: 48px;
    font-family: "Roboto", sans-serif; font-weight: 900;
    font-size: 36px; color: var(--red); letter-spacing: .5px; white-space: nowrap;
  }
  .consult {
    position: absolute; left: 930px; top: 718px;
    font-family: "Oswald", sans-serif; font-weight: 700;
    font-size: 40px; line-height: 1.05; color: var(--ink);
  }
</style>
</head>
<body>
<main class="flyer">
  <header class="header">
    <div class="header__ruler"></div>
    <h1 class="title">Handyman</h1>
    <p class="title__sub">SERVICES</p>
  </header>

  <nav class="band">
    <span>Home Improvement</span><span class="band__dot"></span>
    <span>Garden Services</span><span class="band__dot"></span>
    <span>Repairs</span>
  </nav>

  <div class="badge">
    <span class="badge__ray"></span><span class="badge__ray"></span><span class="badge__ray"></span><span class="badge__ray"></span>
    <div class="badge__disc"></div>
    <div class="badge__art" role="img" aria-label="Illustration of an elderly couple"></div>
    <div class="badge__ribbon">SENIOR CITIZEN<br>DISCOUNT</div>
  </div>

  <aside class="side"></aside>
  <div class="refer">
    <div class="refer__icon" role="img" aria-label="Group of people icon"></div>
    <span class="refer__line">REFER</span>
    <span class="refer__line">a FRIEND!</span>
    <span class="refer__small">GET DISCOUNT</span>
  </div>
  <div class="worker" role="img" aria-label="Cartoon handyman in blue overalls carrying a red toolbox and spanner"></div>

  <section class="services services--left">
    <h2 class="services__heading">Quality Services</h2>
    <ul class="services__list">
      <li class="services__item">Cctv Installation</li>
      <li class="services__item">Decking</li>
      <li class="services__item">Patio/Driveway Cleaning</li>
      <li class="services__item">Garages For Erecting/Repairs</li>
      <li class="services__item">House/Garage Clearances</li>
      <li class="services__item">Fit Alarm Systems</li>
      <li class="services__item">Fit or Repair Windows/Doors</li>
      <li class="services__item">Repair Roofs</li>
      <li class="services__item">Lay Lawns or Repair</li>
      <li class="services__item">Repair/erect Sheds</li>
    </ul>
  </section>

  <section class="services services--right">
    <ul class="services__list">
      <li class="services__item">Decorate Interior/External</li>
      <li class="services__item">Erect Ariaels</li>
      <li class="services__item">Lay Driveways</li>
      <li class="services__item">Erect or Repair Fencing</li>
      <li class="services__item">Lay Drainage</li>
      <li class="services__item">Repair or Erect Guttering and Soffits</li>
      <li class="services__item">Water Features</li>
      <li class="services__item">Erect or Repair Kitchens/Bathrooms</li>
      <li class="services__item">Plastering</li>
      <li class="services__item">Lay Patios</li>
    </ul>
  </section>

  <div class="slogan" role="img" aria-label="Hand lettering: No Job Too Small"></div>

  <div class="call">
    <div class="call__pill">Call Now!</div>
    <svg class="call__icon" viewBox="0 0 88 88" aria-hidden="true">
      <circle cx="44" cy="44" r="40" fill="#e1232a" stroke="#ffffff" stroke-width="4"/>
      <path d="M30 24c4-2 7 0 9 5l2 6c1 3-1 5-3 6 2 6 6 10 12 12 1-2 3-4 6-3l6 2c5 2 7 5 5 9-2 5-7 7-12 6-14-3-25-14-28-28-1-5 0-11 3-15z" fill="#ffffff"/>
    </svg>
    <div class="call__number">07700900482</div>
  </div>

  <p class="consult">For a FREE<br>Consultation</p>
</main>
</body>
</html>
```